Parades of Thunder stationary design

Parades of Thunder (www.paradesofthunder.example) is a company that operates events that display the worlds most exotic cars, motorcyles, aircraft, watercraft and luxury brands. we are cutting edge and are looking for a clean , modern stationary design. our sponsors of the events include names like Veltrano, Morvane, Castelvetro, Kendrix, Bravoni, Lune Varet, Halvorsen and many other big names. we currently operate in florida but are looking to get into new York and California. I added the logo and two car images.car images are optional and not mandatory for the design. Just thought we would add to see what happens.

Target Market(s)

high end , clean design think KENDRIX DESGN style sharp, clean, cutting edge must appeal to the high end luxury brand corporate companies and car, motorcycle, boat, aircraft and luxury brand collectors

Industry/Entity Type

Events

Font styles to use
Sans Serif

Requirements
Must have
• our contact information
• Ray Dunmore
• President
• 352-555-0187
• www.paradesofthunder.example
• PO Box 4862
• Marlow, FL 32190
• for business card my email is ray@paradesofthunder.example

```html
<!DOCTYPE html>
<html lang="en">
<head>
<meta charset="utf-8">
<title>Parades of Thunder — Business Card</title>
<link href="https://fonts.googleapis.com/css2?family=Arimo:wght@400;700&display=swap" rel="stylesheet">
<style>
  :root {
    --backdrop: #e8e8e9;
    --card: #ffffff;
    --ink: #1c1c1c;
    --brand-grey: #8a8a8c;
    --brand-red: #c4161c;
    --car-deep: #4a0c16;
    --car-mid: #8e1e2c;
    --car-light: #c85a66;
    --car-blue: #2d3a8c;
  }
  * { margin: 0; padding: 0; box-sizing: border-box; }
  html, body {
    width: 1116px;
    height: 1200px;
    overflow: hidden;
    background: var(--backdrop);
    font-family: "Arimo", Arial, sans-serif;
    color: var(--ink);
  }
  .sheet { position: relative; width: 1116px; height: 1200px; }
  .card {
    position: absolute;
    left: 155px;
    width: 807px;
    height: 464px;
    background: var(--card);
    overflow: hidden;
  }
  .card--front { top: 95px; }
  .card--back { top: 641px; }

  .holder {
    position: absolute;
    left: 45px;
    top: 48px;
    font-size: 24px;
    line-height: 31px;
  }
  .contact {
    position: absolute;
    left: 413px;
    font-size: 24px;
    line-height: 35px;
  }
  .contact--phone { top: 200px; }
  .contact--post { top: 295px; }
  .contact--online { top: 363px; line-height: 37px; }

  .brand {
    position: absolute;
    left: 43px;
    display: flex;
    align-items: center;
    gap: 12px;
    font-size: 34px;
    font-weight: 700;
    letter-spacing: -0.5px;
    color: var(--brand-grey);
  }
  .card--front .brand { top: 375px; }
  .card--back .brand { top: 365px; }
  .brand__mark {
    width: 14px;
    height: 14px;
    background: var(--brand-red);
  }

  .hero-car {
    position: absolute;
    left: 163px;
    top: 0;
    width: 644px;
    height: 345px;
    background:
      radial-gradient(ellipse 30% 26% at 30% 46%, var(--car-blue) 0%, rgba(45,58,140,0) 100%),
      radial-gradient(ellipse 60% 70% at 55% 35%, var(--car-light) 0%, var(--car-mid) 40%, var(--car-deep) 75%, rgba(255,255,255,0) 100%);
  }
</style>
</head>
<body>
<main class="sheet">
  <section class="card card--front">
    <div class="holder">
      <p class="holder__name">Ray Dunmore</p>
      <p class="holder__title">President</p>
    </div>
    <p class="contact contact--phone">352-555-0187</p>
    <div class="contact contact--post">
      <p>PO Box 4862</p>
      <p>Marlow, FL 32190</p>
    </div>
    <div class="contact contact--online">
      <p>ray@paradesofthunder.example</p>
      <p>www.paradesofthunder.example</p>
    </div>
    <div class="brand"><span class="brand__name">Parades of Thunder</span><span class="brand__mark"></span></div>
  </section>

  <section class="card card--back">
    <div class="hero-car" role="img" aria-label="Photograph of a deep red classic sports car with a blue grille, seen from the front corner"></div>
    <div class="brand"><span class="brand__name">Parades of Thunder</span><span class="brand__mark"></span></div>
  </section>
</main>
</body>
</html>
```